Womans Supplement Designs

Launching a Supplement company and need to get some initial designs created, I've attached our logo and the bottle type that I want the samples done one.

This project is for our Whey Protein we are starting with Vanilla, chocolate and strawberry banana

(ALL DESIGN VARIATIONS MUST BE A WHITE BOTTLE NOT BLACK)

(FOR DESIGN SAMPLES PLEASE USE THE SUPPLEMENT BOTTLE STYLE I PROVIDED)

Whoever is selected the winner I will have more work for you to complete the disigns for the rest of the products in the line, Just want to get this shake completed first

Women

• Must have our current logo involved

the name of this product will be "BLUE OAK"

Must have this slogan,

ALL-IN-ONE PREMIUM PROTEIN NUTRITIONAL SHAKE FOR BLACK WOMEN

This is our meal replacement

the design should try to keep the same look and feel of the existing provided supplement images

we are starting with chocolate, vanilla and strawberry banana

this is for women and should look colorful and appeal to them
• Do not use an image of a person or lady, don't want it branded to a person

```html
<!DOCTYPE html>
<html lang="en">
<head>
<meta charset="utf-8">
<title>Blue Oak Protein Labels</title>
<link href="https://fonts.googleapis.com/css2?family=Russo+One&family=Exo+2:ital,wght@0,400;0,600;0,800;1,800&family=Montserrat:wght@500&display=swap" rel="stylesheet">
<style>
  :root {
    --canvas: #f2f2f3;
    --label-bg: #141414;
    --ink-white: #f4f4f4;
    --ink-grey: #bdbdbd;
    --stripe-dark: #2a2a2a;
    --vanilla: #34c3cc;
    --vanilla-2: #d9f3f5;
    --berry: #ff2e8a;
    --berry-2: #ffc21f;
    --cocoa: #d9a37a;
    --cocoa-2: #8a5a36;
  }
  * { box-sizing: border-box; margin: 0; padding: 0; }
  html, body { width: 1200px; height: 1000px; overflow: hidden; background: var(--canvas); }
  .sheet {
    width: 1200px; height: 1000px;
    display: flex; flex-direction: column; align-items: center; justify-content: center; gap: 20px;
  }
  .label {
    position: relative; width: 1080px; height: 300px;
    background: var(--label-bg); overflow: hidden; border-radius: 6px;
    color: var(--ink-white); font-family: "Exo 2", sans-serif;
  }
  .label--vanilla { --accent: var(--vanilla); --accent-2: var(--vanilla-2); }
  .label--berry { --accent: var(--berry); --accent-2: var(--berry-2); }
  .label--cocoa { --accent: var(--cocoa); --accent-2: var(--cocoa-2); }

  .stripes { position: absolute; inset: 0; width: 100%; height: 100%; }

  .brand {
    position: absolute; top: 34px; left: 0; right: 0; text-align: center;
    font-family: "Montserrat", sans-serif; font-weight: 500; color: var(--ink-white);
    letter-spacing: 0.12em; line-height: 1.25;
  }
  .brand__name { display: block; font-size: 15px; }
  .brand__sub { display: block; font-size: 9px; letter-spacing: 0.35em; }

  .title {
    position: absolute; top: 80px; left: 0; right: 0; text-align: center;
    font-family: "Russo One", sans-serif; font-size: 72px; line-height: 1;
    color: var(--accent); transform: skewX(-10deg);
  }
  .tagline {
    position: absolute; top: 156px; left: 50%; transform: translateX(-50%) skewX(-10deg);
    background: var(--accent); color: var(--label-bg);
    font-weight: 800; font-style: italic; font-size: 14px; padding: 1px 14px;
    white-space: nowrap;
  }
  .shake-line {
    position: absolute; top: 180px; left: 0; right: 0; text-align: center;
    font-size: 19px; font-weight: 400; color: var(--ink-grey); letter-spacing: 0.02em;
  }
  .flavor {
    position: absolute; top: 220px; left: 50%; transform: translateX(-50%);
    width: 230px; border: 2px solid var(--accent); border-radius: 14px;
    text-align: center; padding: 3px 0;
    font-weight: 800; font-style: italic; font-size: 14px; letter-spacing: 0.08em; color: var(--accent);
  }
  .facts { position: absolute; right: 48px; top: 112px; display: flex; flex-direction: column; gap: 5px; align-items: flex-end; }
  .fact {
    width: 58px; border: 2px solid var(--accent); border-radius: 4px;
    text-align: center; padding: 2px 0; line-height: 1;
  }
  .fact__value { display: block; font-weight: 800; font-size: 15px; }
  .fact__unit { display: block; font-size: 7px; letter-spacing: 0.08em; color: var(--ink-grey); margin-top: 2px; }
  .servings { text-align: center; width: 58px; line-height: 1; margin-top: 4px; }
  .servings__count { display: block; font-weight: 800; font-size: 22px; }
  .servings__unit { display: block; font-size: 7px; letter-spacing: 0.08em; color: var(--ink-grey); }
  .net-weight { position: absolute; right: 48px; bottom: 12px; font-size: 10px; color: var(--ink-grey); }
</style>
</head>
<body>
<main class="sheet">

  <section class="label label--berry">
    <svg class="stripes" viewBox="0 0 1080 300" preserveAspectRatio="none" role="img" aria-label="Diagonal chevron stripe pattern in pink and orange">
      <defs>
        <linearGradient id="berry-top" x1="0" y1="0" x2="1" y2="0"><stop offset="0" stop-color="#ff7a3d"/><stop offset="1" stop-color="#ff2e8a"/></linearGradient>
        <linearGradient id="berry-bottom" x1="0" y1="0" x2="1" y2="0"><stop offset="0" stop-color="#ffc21f"/><stop offset="1" stop-color="#ff2e8a"/></linearGradient>
      </defs>
      <polygon points="0,0 380,0 260,90 0,130" fill="#2a2a2a"/>
      <polygon points="600,0 1080,0 1080,110 820,60" fill="url(#berry-top)"/>
      <polygon points="0,200 200,230 320,300 0,300" fill="url(#berry-bottom)"/>
    </svg>
    <div class="brand"><span class="brand__name">NOVA HARBOR</span><span class="brand__sub">LIFESTYLE NUTRITION</span></div>
    <h2 class="title">BLUE OAK</h2>
    <p class="tagline">ALL-IN-ONE PREMIUM PROTEIN</p>
    <p class="shake-line">NUTRITIONAL SHAKE FOR BLACK WOMEN</p>
    <p class="flavor">STRAWBERRY BANANA</p>
    <div class="facts">
      <div class="fact"><span class="fact__value">24g</span><span class="fact__unit">PROTEIN</span></div>
      <div class="fact"><span class="fact__value">5.9</span><span class="fact__unit">BCAAS</span></div>
      <div class="fact"><span class="fact__value">0g</span><span class="fact__unit">SUGAR</span></div>
      <div class="servings"><span class="servings__count">62</span><span class="servings__unit">SERVINGS</span></div>
    </div>
    <p class="net-weight">Net Wt. 1.3kg (3lbs)</p>
  </section>

  <section class="label label--vanilla">
    <svg class="stripes" viewBox="0 0 1080 300" preserveAspectRatio="none" role="img" aria-label="Diagonal chevron stripe pattern in teal and pale aqua">
      <defs>
        <linearGradient id="vanilla-top" x1="0" y1="0" x2="1" y2="0"><stop offset="0" stop-color="#34c3cc"/><stop offset="1" stop-color="#d9f3f5"/></linearGradient>
        <linearGradient id="vanilla-bottom" x1="0" y1="0" x2="1" y2="0"><stop offset="0" stop-color="#34c3cc"/><stop offset="1" stop-color="#d9f3f5"/></linearGradient>
      </defs>
      <polygon points="0,0 380,0 260,90 0,130" fill="#2a2a2a"/>
      <polygon points="600,0 1080,0 1080,110 820,60" fill="url(#vanilla-top)"/>
      <polygon points="0,200 200,230 320,300 0,300" fill="url(#vanilla-bottom)"/>
    </svg>
    <div class="brand"><span class="brand__name">NOVA HARBOR</span><span class="brand__sub">LIFESTYLE NUTRITION</span></div>
    <h2 class="title">BLUE OAK</h2>
    <p class="tagline">ALL-IN-ONE PREMIUM PROTEIN</p>
    <p class="shake-line">NUTRITIONAL SHAKE FOR BLACK WOMEN</p>
    <p class="flavor">VANILLA</p>
    <div class="facts">
      <div class="fact"><span class="fact__value">24g</span><span class="fact__unit">PROTEIN</span></div>
      <div class="fact"><span class="fact__value">5.9</span><span class="fact__unit">BCAAS</span></div>
      <div class="fact"><span class="fact__value">0g</span><span class="fact__unit">SUGAR</span></div>
      <div class="servings"><span class="servings__count">62</span><span class="servings__unit">SERVINGS</span></div>
    </div>
    <p class="net-weight">Net Wt. 1.3kg (3lbs)</p>
  </section>

  <section class="label label--cocoa">
    <svg class="stripes" viewBox="0 0 1080 300" preserveAspectRatio="none" role="img" aria-label="Diagonal chevron stripe pattern in tan and brown">
      <defs>
        <linearGradient id="cocoa-top" x1="0" y1="0" x2="1" y2="0"><stop offset="0" stop-color="#d9a37a"/><stop offset="1" stop-color="#8a5a36"/></linearGradient>
        <linearGradient id="cocoa-bottom" x1="0" y1="0" x2="1" y2="0"><stop offset="0" stop-color="#d9a37a"/><stop offset="1" stop-color="#8a5a36"/></linearGradient>
      </defs>
      <polygon points="0,0 380,0 260,90 0,130" fill="#2a2a2a"/>
      <polygon points="600,0 1080,0 1080,110 820,60" fill="url(#cocoa-top)"/>
      <polygon points="0,200 200,230 320,300 0,300" fill="url(#cocoa-bottom)"/>
    </svg>
    <div class="brand"><span class="brand__name">NOVA HARBOR</span><span class="brand__sub">LIFESTYLE NUTRITION</span></div>
    <h2 class="title">BLUE OAK</h2>
    <p class="tagline">ALL-IN-ONE PREMIUM PROTEIN</p>
    <p class="shake-line">NUTRITIONAL SHAKE FOR BLACK WOMEN</p>
    <p class="flavor">CHOCOLATE</p>
    <div class="facts">
      <div class="fact"><span class="fact__value">24g</span><span class="fact__unit">PROTEIN</span></div>
      <div class="fact"><span class="fact__value">5.9</span><span class="fact__unit">BCAAS</span></div>
      <div class="fact"><span class="fact__value">0g</span><span class="fact__unit">SUGAR</span></div>
      <div class="servings"><span class="servings__count">62</span><span class="servings__unit">SERVINGS</span></div>
    </div>
    <p class="net-weight">Net Wt. 1.3kg (3lbs)</p>
  </section>

</main>
</body>
</html>
```